Redesign of Website

We need an overhaul of our website. I've attached our current logo files. Please visit www.qelvorbis.com for our current website for information about our company. We are looking for the same type of website (information-based only) so no need for any online store, payments, interactive stuff or anything like that...basically looking for a fresh new look! Also please make sure this design will be mobile-friendly. Thanks!

```html
<!DOCTYPE html>
<html lang="en">
<head>
<meta charset="utf-8">
<title>Qelvorbis Consultants, Inc</title>
<link rel="stylesheet" href="https://fonts.googleapis.com/css2?family=Montserrat:wght@400;600;700;800&family=Open+Sans:wght@400;600&display=swap">
<style>
:root{
  --blue:#0b3f8f;
  --blue-dark:#072e6b;
  --green:#7cc576;
  --ink:#2b2b2b;
  --muted:#7a7a7a;
  --grey-bg:#ececec;
  --white:#ffffff;
}
*{box-sizing:border-box;margin:0;padding:0}
html,body{width:1200px;height:3244px;overflow:hidden}
body{font-family:"Open Sans",sans-serif;color:var(--ink);background:var(--white);position:relative}
section,header,footer{position:absolute;left:0;width:1200px}
.site-header{top:0;height:100px;background:var(--white)}
.brand{position:absolute;left:72px;top:18px;display:flex;align-items:center;gap:12px}
.brand-mark{width:52px;height:52px;background:var(--blue);border-radius:50%}
.brand-name{font-family:"Montserrat",sans-serif;font-weight:800;font-size:26px;color:var(--blue);line-height:1}
.brand-name small{display:block;font-size:13px;letter-spacing:2px;margin-top:4px}
.main-nav{position:absolute;right:70px;top:44px;display:flex;gap:8px;font-family:"Montserrat",sans-serif;font-size:14px;font-weight:600;text-transform:uppercase}
.main-nav a{color:var(--blue);text-decoration:none;padding:12px 18px}
.main-nav a.active{background:var(--green);color:var(--white)}
.hero{top:100px;height:620px;overflow:hidden}
.hero-photo{position:absolute;inset:0;background:linear-gradient(160deg,#4a4f55 0%,#2a2e33 45%,#6b6f73 100%)}
.hero-title{position:absolute;top:330px;width:100%;text-align:center;font-family:"Montserrat",sans-serif;font-weight:700;font-size:52px;color:var(--white);letter-spacing:1px}
.btn{display:inline-block;font-family:"Montserrat",sans-serif;font-weight:600;font-size:15px;text-transform:uppercase;color:var(--white);text-decoration:none;border-radius:26px;padding:16px 34px}
.btn-blue{background:var(--blue)}
.hero .btn{position:absolute;top:412px;left:50%;transform:translateX(-50%);border:3px solid var(--green)}
.hero-dots{position:absolute;top:540px;left:50%;transform:translateX(-50%);display:flex;gap:10px}
.hero-dots span{width:40px;height:4px;background:rgba(255,255,255,.5)}
.hero-dots span:first-child{background:var(--white)}
.hero-curve{position:absolute;bottom:0;left:0}
.section-title{font-family:"Montserrat",sans-serif;font-weight:700;font-size:46px;text-align:center;color:var(--blue)}
.section-title em{font-style:normal;color:var(--green)}
.welcome{top:720px;height:540px;text-align:center}
.welcome .section-title{margin-top:90px}
.welcome .sub{font-family:"Montserrat",sans-serif;font-weight:700;font-size:15px;color:var(--blue);letter-spacing:1px}
.welcome p{width:720px;margin:22px auto 0;font-size:15px;line-height:1.75;color:var(--muted)}
.welcome .btn{margin-top:32px;border-radius:4px;padding:16px 30px}
.services{top:1260px;height:510px;background:var(--grey-bg)}
.services .section-title{margin-top:68px}
.service-list{display:flex;justify-content:center;gap:40px;margin-top:34px}
.service{width:200px;text-align:center}
.service-icon{width:130px;height:130px;margin:0 auto;border-radius:50%;border:4px solid var(--blue);background:var(--white);display:flex;align-items:center;justify-content:center}
.service-icon span{width:96px;height:96px;border-radius:50%;border:2px solid var(--green)}
.service h3{font-family:"Montserrat",sans-serif;font-size:15px;font-weight:700;margin-top:22px;color:var(--ink)}
.service p{font-size:13px;line-height:1.6;color:var(--muted);margin-top:10px}
.arrow{position:absolute;top:180px}
.testimonials{top:1770px;height:640px;overflow:hidden;color:var(--white);text-align:center}
.testimonials-photo{position:absolute;inset:0;background:linear-gradient(180deg,#3b3a36 0%,#26251f 100%)}
.testimonials .inner{position:relative}
.testimonials h2{font-family:"Montserrat",sans-serif;font-weight:700;font-size:46px;margin-top:68px}
.testimonials .lead{width:560px;margin:8px auto 0;font-size:14px;line-height:1.6}
.avatar{width:150px;height:150px;margin:36px auto 0;border-radius:50%;border:5px solid var(--green);background:linear-gradient(180deg,#9aa6b2,#55606b)}
.quote-mark{position:absolute;left:212px;top:410px;font-family:"Montserrat",sans-serif;font-size:110px;font-weight:800;color:var(--green);line-height:1}
.quote{width:600px;margin:36px auto 0;font-size:15px;font-style:italic;line-height:1.6}
.cite{margin-top:28px;font-family:"Montserrat",sans-serif;color:var(--green);font-weight:600;font-size:16px;letter-spacing:1px}
.cite small{display:block;color:var(--white);font-size:13px;margin-top:4px}
.slide-btn{position:absolute;top:310px;width:48px;height:48px;border-radius:50%;border:2px solid var(--white)}
.contact{top:2410px;height:490px;text-align:center}
.contact .section-title{margin-top:78px}
.contact .lead{font-size:14px;color:var(--muted);margin-top:6px}
.contact-form{position:relative;width:720px;margin:30px auto 0;height:200px}
.field{position:absolute;border:1px solid #cfcfcf;background:var(--white);font-size:13px;color:#999;text-align:left;padding:12px 14px}
.contact .btn{position:absolute;left:50%;transform:translateX(-50%);top:388px;background:var(--green);border-radius:4px;padding:12px 40px}
.site-footer{top:2900px;height:344px;background:var(--blue);color:var(--white)}
.foot-cols{display:flex;gap:60px;padding:56px 0 0 80px}
.foot-col h4{font-family:"Montserrat",sans-serif;font-size:16px;font-weight:700;text-transform:uppercase;margin-bottom:20px}
.foot-col ul{list-style:none;font-size:14px;line-height:2}
.foot-row{display:flex;gap:12px;align-items:flex-start;font-size:14px;line-height:1.5;margin-bottom:18px}
.foot-row svg{flex:none}
.foot-col p{font-size:14px;line-height:1.6;width:210px}
.subscribe{display:flex;margin-top:18px}
.subscribe span{width:160px;height:40px;background:var(--white);color:#999;font-size:13px;padding:11px 12px}
.subscribe i{width:44px;height:40px;background:var(--green);display:flex;align-items:center;justify-content:center}
.foot-brand{text-align:center;width:220px}
.foot-brand .brand-name{color:var(--white);font-size:24px}
.foot-brand .phone-ring{width:54px;height:54px;border-radius:50%;background:var(--green);margin:18px auto 10px;display:flex;align-items:center;justify-content:center}
.foot-brand strong{font-family:"Montserrat",sans-serif;font-size:26px}
.copyright{position:absolute;bottom:0;width:100%;height:44px;background:var(--blue-dark);text-align:center;font-size:13px;line-height:44px}
</style>
</head>
<body>

<header class="site-header">
  <div class="brand"><span class="brand-mark"></span><span class="brand-name">QELVORBIS<small>CONSULTANTS</small></span></div>
  <nav class="main-nav">
    <a class="active" href="#">Home</a><a href="#">About Qelvorbis</a><a href="#">Our Services</a><a href="#">Qelvorbis News</a><a href="#">Contact Us</a>
  </nav>
</header>

<section class="hero">
  <div class="hero-photo" role="img" aria-label="Business professionals reviewing documents with a city skyline overlay"></div>
  <h1 class="hero-title">QELVORBIS CONSULTANTS, INC</h1>
  <a class="btn btn-blue" href="#">Get Started</a>
  <div class="hero-dots"><span></span><span></span><span></span></div>
  <svg class="hero-curve" width="1200" height="60" viewBox="0 0 1200 60"><path d="M0 40 Q600 -10 1200 20 L1200 60 L0 60Z" fill="#ffffff"/></svg>
</section>

<section class="welcome">
  <h2 class="section-title">WELCOME <em>TO</em> QELVORBIS</h2>
  <div class="sub">CONSULTANTS</div>
  <p>With over 25 years of experience we provide consistent and comprehensive inspection services to financial institutions involved in construction and loan management in New York, New Jersey, Pennsylvania and surrounding areas.</p>
  <p>The firm's professional staff bring years of engineering, environmental, building and real estate experience to work for our clients.</p>
  <p>Qelvorbis provides our clients with in-depth plan and cost, construction lending, environmental and property condition reports.</p>
  <a class="btn btn-blue" href="#">Learn More</a>
</section>

<section class="services">
  <h2 class="section-title">OUR <em>SERVICES</em></h2>
  <svg class="arrow" style="left:40px" width="20" height="30" viewBox="0 0 20 30"><path d="M16 3 L4 15 L16 27" stroke="#555" stroke-width="3" fill="none"/></svg>
  <svg class="arrow" style="right:40px" width="20" height="30" viewBox="0 0 20 30"><path d="M4 3 L16 15 L4 27" stroke="#555" stroke-width="3" fill="none"/></svg>
  <div class="service-list">
    <div class="service"><div class="service-icon"><span></span></div><h3>PROPERTY CONDITION REPORTING</h3><p>Before buying almost any real estate, financial institutions need to know the full condition.</p></div>
    <div class="service"><div class="service-icon"><span></span></div><h3>PLAN &amp; COST REVIEWS</h3><p>Our Plan &amp; Cost Reviews provide lending institutions with expert analysis of new construction.</p></div>
    <div class="service"><div class="service-icon"><span></span></div><h3>CONSTRUCTION FUNDING INSPECTIONS</h3><p>Lending institutions rely on our employees with the expertise needed to evaluate progress.</p></div>
    <div class="service"><div class="service-icon"><span></span></div><h3>ENVIRONMENTAL TRANSACTION SCREENS</h3><p>Environmental Transaction Screens provide an economical and meaningful review.</p></div>
  </div>
</section>

<section class="testimonials">
  <div class="testimonials-photo" role="img" aria-label="Team meeting around a table in a dim office"></div>
  <div class="inner">
    <h2>TESTIMONIALS</h2>
    <p class="lead">Clients share what working with our inspection team is like, from first call to final report delivered.</p>
    <div class="avatar" role="img" aria-label="Client portrait"></div>
    <div class="quote-mark">&ldquo;</div>
    <p class="quote">Reports always arrive on time, clear and thorough. Their staff answers every question quickly and the site visits are handled with care, making our lending decisions much easier each season.</p>
    <div class="cite">- MARA KELLEN<small>Los Angeles , NY</small></div>
  </div>
  <div class="slide-btn" style="left:40px"></div>
  <div class="slide-btn" style="right:40px"></div>
</section>

<section class="contact">
  <h2 class="section-title">CONTACT <em>US</em></h2>
  <p class="lead">If You Have Any Question for Contact Us Today !</p>
  <div class="contact-form">
    <div class="field" style="left:0;top:0;width:190px;height:40px">Name *</div>
    <div class="field" style="left:0;top:58px;width:190px;height:40px">Email *</div>
    <div class="field" style="left:0;top:116px;width:190px;height:40px">Phone *</div>
    <div class="field" style="left:210px;top:0;width:510px;height:160px">Message *</div>
  </div>
  <a class="btn" href="#">Submit</a>
</section>

<footer class="site-footer">
  <div class="foot-cols">
    <div class="foot-col"><h4>Sitemap</h4><ul><li>› Home</li><li>› About Us</li><li>› Services</li><li>› Contact Us</li></ul></div>
    <div class="foot-col"><h4>Contact Us</h4>
      <div class="foot-row"><svg width="16" height="20" viewBox="0 0 16 20"><path d="M8 0a7 7 0 0 0-7 7c0 5 7 13 7 13s7-8 7-13a7 7 0 0 0-7-7zm0 10a3 3 0 1 1 0-6 3 3 0 0 1 0 6z" fill="#7cc576"/></svg><span>48 Larkmoor Ave Suite 12<br>Fenwick Township, NJ 07990</span></div>
      <div class="foot-row"><svg width="16" height="16" viewBox="0 0 16 16"><path d="M3 1l3 3-2 2c1 2 3 4 5 5l2-2 3 3-2 3C6 15 1 10 1 3z" fill="#7cc576"/></svg><span>973-555-0148</span></div>
      <div class="foot-row"><svg width="16" height="12" viewBox="0 0 16 12"><rect x="0.5" y="0.5" width="15" height="11" fill="none" stroke="#7cc576"/><path d="M1 1l7 6 7-6" stroke="#7cc576" fill="none"/></svg><span>info@qelvorbis.com</span></div>
    </div>
    <div class="foot-col"><h4>Newsletter</h4><p>Would you like to receive our exclusive news and update the sign up our newsletter?</p>
      <div class="subscribe"><span>Enter Email</span><i><svg width="14" height="14" viewBox="0 0 14 14"><path d="M3 1l7 6-7 6" stroke="#fff" stroke-width="2" fill="none"/></svg></i></div>
    </div>
    <div class="foot-brand"><span class="brand-name">QELVORBIS CONSULTANTS</span>
      <div class="phone-ring"><svg width="24" height="24" viewBox="0 0 16 16"><path d="M3 1l3 3-2 2c1 2 3 4 5 5l2-2 3 3-2 3C6 15 1 10 1 3z" fill="#fff"/></svg></div>
      <strong>973-555-0148</strong>
    </div>
  </div>
  <div class="copyright">© 2016 QELVORBIS CONSULTANTS , All Rights Reserved.</div>
</footer>

</body>
</html>
```